New Business Card Design

We would like to refresh our business cards and make them look better. We are an IT company specialising in Cloud Services, IT Managed Services, software and hardware. I have attached a PSD of our current design. Also attached our logo.
Updates

I have uploaded all new logos in EPS format.

Can you please edit all designs to include a job title for Marcus Hale, eg. General Manager

Industry/Entity Type

Software

Colors
ffffff

Requirements
Must have
• Please use white background.
Should not have
• Black background

```html
<!DOCTYPE html>
<html lang="en">
<head>
<meta charset="utf-8">
<title>Corvan Technology – Business Card</title>
<link rel="stylesheet" href="https://fonts.googleapis.com/css2?family=Jost:ital,wght@0,400;0,500;0,700;1,600&display=swap">
<style>
  :root {
    --page: #ffffff;
    --card-edge: #9a9a9a;
    --card-light: #f8f8f8;
    --card-mid: #ececec;
    --card-dark: #dedede;
    --accent-red: #c0443a;
    --ink: #35383d;
    --navy: #0f1b2d;
    --navy-soft: #3c4a62;
    --label: #000000;
  }
  * { margin: 0; padding: 0; box-sizing: border-box; }
  html, body {
    width: 1000px; height: 1200px; overflow: hidden;
    background: var(--page);
  }
  .sheet { position: relative; width: 1000px; height: 1200px; }
  .card {
    position: absolute; left: 130px; width: 736px; height: 420px;
    border: 1px solid var(--card-edge);
    overflow: hidden;
  }
  .card--front {
    top: 44px;
    background: linear-gradient(100deg, var(--card-dark) 0%, var(--card-mid) 35%, var(--card-light) 70%, #fafafa 100%);
  }
  .card--back {
    top: 662px;
    background: linear-gradient(75deg, #fbfbfb 0%, var(--card-mid) 55%, var(--card-dark) 100%);
  }
  .side-label {
    position: absolute; left: 0; width: 1000px; text-align: center;
    font-family: Arial, Helvetica, sans-serif; font-size: 44px; color: var(--label);
  }
  .side-label--front { top: 482px; }
  .side-label--back { top: 1094px; }

  .holder { position: absolute; left: 31px; top: 124px; font-family: "Jost", sans-serif; }
  .holder__name {
    font-size: 35px; font-weight: 700; color: var(--accent-red);
    letter-spacing: 0.5px; line-height: 1;
  }
  .holder__title {
    margin-top: 4px; font-size: 24px; font-weight: 600; font-style: italic;
    color: var(--ink); line-height: 1;
  }
  .contacts { position: absolute; left: 33px; top: 224px; list-style: none; font-family: "Jost", sans-serif; }
  .contacts__item {
    display: flex; align-items: center; height: 31px;
    font-size: 25px; color: var(--accent-red); letter-spacing: 0.3px;
  }
  .contacts__icon { width: 22px; height: 22px; margin-right: 9px; fill: var(--ink); }
  .dot-band { position: absolute; left: 0; bottom: 0; }

  .brand { position: absolute; left: 0; top: 0; width: 736px; height: 420px; font-family: "Jost", sans-serif; text-align: center; }
  .brand__name {
    position: absolute; left: 0; top: 258px; width: 736px;
    font-size: 36px; font-weight: 400; letter-spacing: 7px; color: var(--ink);
  }
  .brand__web {
    position: absolute; left: 0; top: 325px; width: 736px;
    font-size: 23px; letter-spacing: 2px; color: var(--accent-red);
  }
</style>
</head>
<body>
<main class="sheet">
  <section class="card card--front" aria-label="Card front">
    <div class="holder">
      <p class="holder__name">MARCUS HALE</p>
      <p class="holder__title">General Manager</p>
    </div>
    <ul class="contacts">
      <li class="contacts__item">
        <svg class="contacts__icon" viewBox="0 0 22 22" aria-hidden="true"><rect x="2" y="6" width="18" height="11" rx="1"/><path d="M2.8 6.8 11 13l8.2-6.2" fill="none" stroke="#fff" stroke-width="1.3"/></svg>
        mhale@corvanit.com.au
      </li>
      <li class="contacts__item">
        <svg class="contacts__icon" viewBox="0 0 22 22" aria-hidden="true"><path d="M6 2c1 0 2.5 3 2.5 4S7 7.5 7 8.5c0 1.5 3.5 6.5 5 6.5 1 0 1.5-1.5 2.5-1.5s3.5 2 3.5 3-1.5 3.5-3.5 3.5C9 20 3 11 3 6c0-2 2-4 3-4z"/></svg>
        07 3000 4812
      </li>
      <li class="contacts__item">
        <svg class="contacts__icon" viewBox="0 0 22 22" aria-hidden="true"><rect x="5" y="1" width="12" height="20" rx="2"/><rect x="7" y="4" width="8" height="8" fill="#fff"/><rect x="7" y="14" width="8" height="5" fill="#fff" opacity=".5"/></svg>
        0400 215 673
      </li>
    </ul>
    <svg class="dot-band" width="736" height="110" viewBox="0 0 736 110" role="img" aria-label="Halftone dot band rising from left to right">
      <defs>
        <linearGradient id="band-fade" x1="0" y1="0" x2="0" y2="1">
          <stop offset="0" stop-color="#3c4a62"/>
          <stop offset="0.35" stop-color="#0f1b2d"/>
          <stop offset="1" stop-color="#0f1b2d"/>
        </linearGradient>
      </defs>
      <polygon points="0,80 736,6 736,110 0,110" fill="url(#band-fade)"/>
    </svg>
  </section>
  <p class="side-label side-label--front">FRONT</p>

  <section class="card card--back" aria-label="Card back">
    <div class="brand">
      <p class="brand__name">corvan technology</p>
      <p class="brand__web">www.corvanit.com.au</p>
    </div>
  </section>
  <p class="side-label side-label--back">BACK</p>
</main>
</body>
</html>
```